Artificial intelligence, machine learning, and automation company needs a sexy business card design

We need a sleek and sexy business card design for an AI consulting company based in Philadelphia PA. We provide custom machine learning and automation solutions for companies of all shapes and sizes. The primary industries that we serve are pharmaceuticals, engineering, healthcare, and computer software. We would like the designs to be a black business card that uses green as a sleek accent color. The final design should communicate intelligence, cutting edge new-tech, and optimization.

Target Market(s)

C-level and VP level executives of multi-million annual companies. Mostly in Pharma, Healthcare, Real Estate, Retail, and Engineering

Industry/Entity Type

Computer Software

Contact Information for Business Card

Name: Jed Harlow
Title: CEO
Cell: 484 562 0937
Email: JedH@quillorbit.example
Website: www.QuillOrbit.example

Font styles to use
Sans Serif

Colors

Designer to choose colors to be used in the design.

Requirements
Must have
• 1) Attached Quillon Logo (either with colors or not/embossed)
• 2) "Artificial Intelligence" "Automation" and "Machine Learning"
• 3) "Quillon Laboratories" or "Quillon Labs" or "Quillon"
• 4) Sexy AF.
Nice to have
• Black card / dark card color, "Quillon Green" accent colors (in attached .ai file), Embossment of logo/name/etc, thick card stock, colored borders (on card sides, not front/back faces)
Should not have
• Should not be bland, or unsexy.

```html
<!DOCTYPE html>
<html lang="en">
<head>
<meta charset="UTF-8">
<title>Quillon Laboratories – Business Card</title>
<link href="https://fonts.googleapis.com/css2?family=Open+Sans:wght@400;700&display=swap" rel="stylesheet">
<style>
  :root {
    --stage: #1c1c1c;
    --card: #050505;
    --card-edge: #2a2a2a;
    --ink: #ffffff;
    --accent: #6cc7b6;
  }
  * { box-sizing: border-box; margin: 0; padding: 0; }
  html, body { width: 1200px; height: 1000px; overflow: hidden; }
  body {
    background: var(--stage);
    font-family: "Open Sans", Arial, sans-serif;
    color: var(--ink);
    position: relative;
  }
  .card {
    position: absolute;
    top: 345px;
    width: 540px;
    height: 309px;
    border-radius: 22px;
    background: var(--card);
    box-shadow: 0 0 0 1px var(--card-edge);
    overflow: hidden;
  }
  .card--front { left: 40px; }
  .card--back { left: 620px; }

  /* Front */
  .brand {
    position: absolute;
    left: 150px;
    top: 62px;
    display: flex;
    align-items: center;
    gap: 18px;
  }
  .brand__square {
    width: 64px;
    height: 64px;
    border: 3px solid var(--ink);
  }
  .brand__name {
    font-weight: 400;
    color: var(--ink);
    text-transform: uppercase;
    line-height: 1.05;
  }
  .brand__name-main { display: block; font-size: 44px; letter-spacing: 9px; }
  .brand__name-sub { display: block; font-size: 18px; letter-spacing: 6px; }
  .span-arrow {
    position: absolute;
    left: 26px;
    top: 196px;
  }
  .services {
    position: absolute;
    left: 32px;
    top: 226px;
    font-size: 15px;
    letter-spacing: 0.3px;
  }

  /* Back */
  .person {
    position: absolute;
    left: 40px;
    top: 34px;
  }
  .person__name {
    font-size: 27px;
    font-weight: 700;
    color: var(--accent);
    letter-spacing: 0.5px;
  }
  .person__title {
    font-size: 13px;
    margin-top: 2px;
  }
  .back-brand {
    position: absolute;
    left: 40px;
    top: 150px;
    font-size: 20px;
    font-weight: 400;
    color: var(--accent);
    letter-spacing: 3px;
    text-transform: uppercase;
  }
  .contact {
    position: absolute;
    right: 100px;
    bottom: 36px;
    text-align: right;
    font-size: 17px;
    line-height: 1.3;
    letter-spacing: 0.3px;
  }
  .rise-arrow {
    position: absolute;
    left: 440px;
    top: 20px;
  }
</style>
</head>
<body>
  <section class="card card--front" aria-label="Card front">
    <div class="brand">
      <div class="brand__square"></div>
      <div class="brand__name">
        <span class="brand__name-main">Quillon</span>
        <span class="brand__name-sub">Laboratories</span>
      </div>
    </div>
    <svg class="span-arrow" width="490" height="16" viewBox="0 0 490 16" aria-hidden="true">
      <line x1="4" y1="8" x2="486" y2="8" stroke="var(--accent)" stroke-width="2"/>
      <path d="M12 2 L3 8 L12 14" fill="none" stroke="var(--accent)" stroke-width="2"/>
      <path d="M478 2 L487 8 L478 14" fill="none" stroke="var(--accent)" stroke-width="2"/>
    </svg>
    <p class="services">Artificial Intelligence | Automation | Machine Learning</p>
  </section>

  <section class="card card--back" aria-label="Card back">
    <div class="person">
      <h1 class="person__name">Jed Harlow</h1>
      <p class="person__title">CEO</p>
    </div>
    <p class="back-brand">Quillon</p>
    <address class="contact" style="font-style:normal">
      <div>484 562 0937</div>
      <div>JedH@quillorbit.example</div>
      <div>www.QuillOrbit.example</div>
    </address>
    <svg class="rise-arrow" width="90" height="280" viewBox="0 0 90 280" aria-hidden="true">
      <line x1="60" y1="268" x2="60" y2="14" stroke="var(--accent)" stroke-width="9" stroke-linecap="round"/>
      <path d="M40 40 L60 12 L80 40" fill="none" stroke="var(--accent)" stroke-width="9" stroke-linecap="round" stroke-linejoin="round"/>
      <line x1="34" y1="268" x2="34" y2="180" stroke="var(--accent)" stroke-width="7" stroke-linecap="round"/>
    </svg>
  </section>
</body>
</html>
```